Velvet Pier Gig, Guaranteed Project

Night Club Flyer. (Need all the text, this was mis-characterized as a logo but it's a flyer. Any ideas are fine, the flyer we submitted is just a draft with the info but we want a new flyer design. Can be anything as long as it has all the text. For examples of what I like visit www.loomfield-beats.com

Target Market(s)

21 and over house/electronic music audience

Industry/Entity Type

Night Club

Logo Text

Text is on the sample

Logo styles of interest
Abstract Logo
Font styles to use
Sans Serif

Colors

Designer to choose colors to be used in the design.

Requirements
Must have
• All the text from the flyer included.
Nice to have
• Female model, classy not sexy (not mandatory). Focus should be on the band, dj's and velvet pier

```html
<!DOCTYPE html>
<html lang="en">
<head>
<meta charset="utf-8">
<title>Subtide – Velvet Pier Night Club Flyer</title>
<link rel="stylesheet" href="https://fonts.googleapis.com/css2?family=Audiowide&family=Quicksand:wght@500;700&family=Josefin+Sans:wght@600;700&display=swap">
<style>
  :root {
    --page-bg: #e6ebee;
    --night-deep: #150a3a;
    --night-violet: #3a1670;
    --night-blue: #1b3c8c;
    --glow-cyan: #3fc6e0;
    --glow-magenta: #b02fa8;
    --gold: #e9c77a;
    --silver: #e4e6ef;
    --white: #ffffff;
    --muted: #b9b3d8;
    --live-red: #d6283c;
    --band-dark: #120828;
  }
  * { margin: 0; padding: 0; box-sizing: border-box; }
  html, body { width: 1200px; height: 894px; overflow: hidden; background: var(--page-bg); }
  .canvas { position: relative; width: 1200px; height: 894px; }

  .flyer {
    position: absolute; left: 275px; top: 27px; width: 650px; height: 840px; overflow: hidden;
    background:
      radial-gradient(circle at 70% 30%, rgba(63,198,224,0.35), transparent 45%),
      radial-gradient(circle at 25% 60%, rgba(176,47,168,0.45), transparent 50%),
      linear-gradient(160deg, var(--night-violet), var(--night-deep) 60%, var(--night-blue));
    box-shadow: 0 18px 40px rgba(20,10,50,0.35);
    color: var(--white);
  }

  .tagline-arc { position: absolute; left: 0; top: 0; width: 650px; height: 200px; }
  .tagline-arc text { font-family: "Josefin Sans", sans-serif; font-weight: 700; font-size: 16px; fill: var(--gold); letter-spacing: 1px; }

  .event-title {
    position: absolute; left: 175px; top: 140px;
    font-family: "Audiowide", sans-serif; font-size: 80px; line-height: 1;
    color: var(--silver); letter-spacing: 2px; white-space: nowrap;
    transform: rotate(-6deg); transform-origin: left bottom;
  }
  .event-date {
    position: absolute; left: 400px; top: 238px;
    font-family: "Josefin Sans", sans-serif; font-weight: 700; font-size: 26px; color: var(--gold);
    white-space: nowrap;
  }

  .model-photo {
    position: absolute; left: 40px; top: 260px; width: 320px; height: 380px;
    background:
      radial-gradient(ellipse at 50% 30%, #c79a86 0%, #7a4e5c 35%, transparent 65%),
      linear-gradient(180deg, #4a2a55, #2a1240);
    border-radius: 4px;
  }

  .lineup { position: absolute; left: 385px; top: 292px; width: 250px; }
  .dj { margin-bottom: 20px; }
  .dj-name { font-family: "Quicksand", sans-serif; font-weight: 700; font-size: 40px; line-height: 1; color: var(--white); white-space: nowrap; }
  .dj-home { font-family: "Quicksand", sans-serif; font-weight: 500; font-size: 13px; color: var(--muted); letter-spacing: 1px; text-transform: uppercase; margin-top: 4px; padding-left: 4px; white-space: nowrap; }
  .live-set {
    display: inline-block; margin-right: 10px; padding: 3px 8px; border-radius: 3px;
    background: var(--live-red); color: var(--white);
    font-family: "Josefin Sans", sans-serif; font-weight: 700; font-size: 12px; letter-spacing: 1px;
  }

  .club-badge {
    position: absolute; left: 505px; top: 560px; width: 110px; height: 62px;
    border-radius: 50%; border: 2px solid var(--silver); background: rgba(255,255,255,0.08);
  }

  .venue-mark {
    position: absolute; left: 50px; top: 660px; display: flex; align-items: center; gap: 8px;
    font-family: "Josefin Sans", sans-serif; font-weight: 700; font-size: 24px; color: var(--white);
    white-space: nowrap;
  }
  .venue-mark .dot { width: 12px; height: 12px; border-radius: 50%; background: var(--white); }

  .info { position: absolute; left: 250px; top: 650px; display: flex; align-items: center; gap: 10px; }
  .info-label { font-family: "Quicksand", sans-serif; font-weight: 700; font-size: 22px; color: var(--white); }
  .info-links { font-family: "Josefin Sans", sans-serif; font-weight: 700; font-size: 15px; line-height: 1.5; color: var(--white); white-space: nowrap; }

  .venue-band {
    position: absolute; left: 0; top: 715px; width: 650px; height: 125px;
    background: linear-gradient(180deg, rgba(18,8,40,0.2), var(--band-dark) 35%);
    padding: 30px 30px 0;
    font-family: "Josefin Sans", sans-serif; color: var(--gold);
  }
  .venue-headline { font-weight: 700; font-size: 25px; letter-spacing: 0.5px; white-space: nowrap; }
  .venue-address { font-weight: 600; font-size: 15px; margin-top: 12px; white-space: nowrap; }
</style>
</head>
<body>
<main class="canvas">
  <article class="flyer">
    <svg class="tagline-arc" viewBox="0 0 650 200">
      <defs><path id="tagline-path" d="M 30 150 Q 300 40 625 55"/></defs>
      <text textLength="580" lengthAdjust="spacingAndGlyphs"><textPath href="#tagline-path">COME PARTY AFTER THE HARBOR SHARKS BEAT THE BAY COMETS!</textPath></text>
    </svg>

    <h1 class="event-title">SUBTIDE</h1>
    <p class="event-date">July 14th 2017</p>

    <div class="model-photo" role="img" aria-label="Photo of a woman in a sequined dress wearing DJ headphones"></div>

    <section class="lineup">
      <div class="dj"><p class="dj-name">velour</p><p class="dj-home">San Francisco</p></div>
      <div class="dj"><p class="dj-name">mr.kestrel</p><p class="dj-home">Bay Area</p></div>
      <div class="dj"><p class="dj-name">eco marea</p><p class="dj-home"><span class="live-set">LIVE SET</span>San Diego</p></div>
    </section>

    <div class="club-badge"></div>

    <div class="venue-mark"><span class="dot"></span>Velvet Pier</div>

    <div class="info">
      <span class="info-label">info</span>
      <svg width="16" height="18" viewBox="0 0 16 18"><polygon points="0,0 16,9 0,18" fill="var(--live-red)"/></svg>
      <p class="info-links">www.loomfield-beats.com<br>ecomarea-sound.com</p>
    </div>

    <footer class="venue-band">
      <p class="venue-headline">LIVE AT THE VELVET PIER HOTEL – CLUB 48</p>
      <p class="venue-address">48 Tidewater Ave, Harbor City, CA 90000 • T: 555-210-4400 &nbsp;R: 555-318-2290</p>
    </footer>
  </article>
</main>
</body>
</html>
```